Cool modern, tech Business card design

Looking for a new business card design for our Managed IT Services company. We would like 2 sides, with the logo one one side horizontally and then the information on the back in either vertical or horizontal. We want our colors from the logo incorporated but also would like to see the color gray in there as well.

Target Market(s)

IT, Information Technology, Tech, Service

Industry/Entity Type

It Service

Contact Information for Business Card

Carl Penner
Managing Partner
(P)555-271-4830 ext xxx
(F)555-271-4831
www.brixtelcore.com

Font styles to use
Sans Serif

Colors
959595
000000
ec1f27

Requirements
Must have
• Logo on one side with some nice design or pattern
• Information on back in either vertical or horizontal format
Nice to have
• For it to look cool, tech, modern, stand out.

```html
<!DOCTYPE html>
<html lang="en">
<head>
<meta charset="utf-8">
<title>Brixtelcore business card</title>
<link rel="stylesheet" href="https://fonts.googleapis.com/css2?family=Work+Sans:wght@400;500;600&display=swap">
<style>
  :root {
    --stage: #1c1c1d;
    --card-edge: #2a2a2c;
    --brand-red: #ec1f27;
    --brand-gray: #959595;
    --ink-light: #f2f2f2;
    --ink-soft: #d6d6d6;
    --emboss-light: rgba(220,220,220,.55);
    --emboss-dark: rgba(10,10,10,.9);
  }
  * { box-sizing: border-box; margin: 0; padding: 0; }
  html, body {
    width: 1200px; height: 900px; overflow: hidden;
    background: var(--stage);
    font-family: "Work Sans", Arial, sans-serif;
  }
  .stage {
    position: relative; width: 1200px; height: 900px;
    display: flex; flex-direction: column; align-items: center; justify-content: center; gap: 48px;
  }
  .card {
    position: relative; width: 640px; height: 366px; overflow: hidden;
    background: linear-gradient(135deg, #161617 0%, #1f1f21 60%, #2a2a2c 100%);
    border: 1px solid var(--card-edge);
    box-shadow: 0 18px 40px rgba(0,0,0,.55);
  }

  /* front side */
  .card-front { display: flex; flex-direction: column; align-items: center; justify-content: center; gap: 18px; }
  .front-graphic {
    width: 240px; height: 80px; border-radius: 40px;
    background: radial-gradient(ellipse at 55% 50%, rgba(150,150,150,.35) 0%, rgba(60,60,62,.25) 55%, rgba(30,30,32,0) 100%);
  }
  .wordmark { display: flex; align-items: center; gap: 14px; margin-bottom: 20px; }
  .wordmark-name {
    font-weight: 500; font-size: 66px; letter-spacing: -1px; color: var(--brand-gray); line-height: 1;
  }
  .wordmark-square { width: 26px; height: 26px; background: var(--brand-gray); border-radius: 5px; }

  /* back side */
  .card-back { padding: 38px 44px; }
  .back-graphic {
    position: absolute; left: 330px; top: 110px; width: 280px; height: 240px; border-radius: 28px;
    background:
      radial-gradient(ellipse at 70% 30%, var(--emboss-light) 0%, rgba(120,120,120,.25) 35%, rgba(40,40,42,0) 70%),
      radial-gradient(ellipse at 25% 75%, var(--emboss-dark) 0%, rgba(20,20,20,0) 60%);
  }
  .back-content { position: relative; }
  .back-wordmark {
    font-weight: 500; font-size: 56px; letter-spacing: -1px; color: var(--ink-light); line-height: 1;
  }
  .person { margin-top: 28px; }
  .person-name {
    font-weight: 500; font-size: 30px; color: var(--brand-red); text-transform: uppercase; line-height: 1.1;
  }
  .person-title { font-size: 17px; color: var(--ink-light); letter-spacing: .5px; }
  .address { margin-top: 14px; font-size: 17px; color: var(--ink-soft); line-height: 1.35; letter-spacing: .4px; }
  .contact-list { list-style: none; margin-top: 12px; font-size: 17px; color: var(--ink-light); line-height: 1.4; letter-spacing: .3px; }
  .contact-list li { display: flex; align-items: center; gap: 10px; }
  .contact-icon { width: 12px; height: 12px; flex: none; fill: none; stroke: var(--brand-red); stroke-width: 1.6; }
</style>
</head>
<body>
<main class="stage">
  <section class="card card-front" aria-label="Card front">
    <div class="front-graphic" role="img" aria-label="Embossed brand graphic above the name"></div>
    <div class="wordmark">
      <span class="wordmark-name">brixtelcore</span>
      <span class="wordmark-square" aria-hidden="true"></span>
    </div>
  </section>

  <section class="card card-back" aria-label="Card back">
    <div class="back-graphic" role="img" aria-label="Large embossed brand graphic in glossy gray"></div>
    <div class="back-content">
      <div class="back-wordmark">brixtelcore</div>
      <div class="person">
        <h1 class="person-name">Carl Penner</h1>
        <p class="person-title">Managing Partner</p>
      </div>
      <p class="address">42 Alder Lane<br>Millbrook, New York 11290</p>
      <ul class="contact-list">
        <li>
          <svg class="contact-icon" viewBox="0 0 12 12" aria-hidden="true"><path d="M3 1 L5 3.5 L4 5 Q5.5 7.5 7 8 L8.5 7 L11 9 L9.5 11 Q4 10 1 3 Z"/></svg>
          555-271-4830 ext xxx
        </li>
        <li>
          <svg class="contact-icon" viewBox="0 0 12 12" aria-hidden="true"><rect x="3" y="1" width="6" height="3"/><rect x="1" y="4" width="10" height="5"/><rect x="3" y="8" width="6" height="3"/></svg>
          555-271-4831
        </li>
        <li>
          <svg class="contact-icon" viewBox="0 0 12 12" aria-hidden="true"><rect x="1" y="2.5" width="10" height="7"/><path d="M1 2.5 L6 6.5 L11 2.5"/></svg>
          info@brixtelcore.com
        </li>
        <li>
          <svg class="contact-icon" viewBox="0 0 12 12" aria-hidden="true"><circle cx="6" cy="6" r="5"/><ellipse cx="6" cy="6" rx="2.2" ry="5"/><path d="M1 6 H11"/></svg>
          www.brixtelcore.com
        </li>
      </ul>
    </div>
  </section>
</main>
</body>
</html>
```